Alaska Law Firm Needs a Sticker Design

We need a design for stickers to put on already-printed brochures. We mail the brochures to potential clients so they can learn more about accident-induced injuries, insurance claims, legal representation, and our own law firm.

One of our lawyers wrote a book that provides a helpful overview of personal injury claims. We are offering this book for free to anyone who calls and requests it. Therefore, the sticker design should include one of the following phrases, or something very similar:
a) "Still have questions? Call and request our book-- for free!"
b) "Still have questions about auto accident claims? Call and request our book today."
c) "Still have questions about filing a claim? Call and request a free copy of our book."
d) "Still have questions? Call us today to request a free copy of our book, Clear Lanes Ahead."
e) "To learn more about automobile accidents and insurance, call today and request a free copy of our book."

The sticker should be approximately 3"x3" and may be a circle, square, rectangle, or ellipsis. The sticker will be placed on the back of the folder, which is light blue. We would like the sticker to match the color scheme of our website and the folder.

I will upload an image of the book cover as soon as I obtain it.

Industry/Entity Type

Law Firm

Font styles to use
Serif
Sans Serif

Requirements
Should not have
• Bright colors that aren't already used in the folder design. e.g. no bright orange, pink, chartreuse, turquoise, yellow, red.

```html
<!DOCTYPE html>
<html lang="en">
<head>
<meta charset="utf-8">
<title>Still Have Questions? Sticker</title>
<link href="https://fonts.googleapis.com/css2?family=Cinzel:wght@400;500&family=Open+Sans:wght@400;600;800&display=swap" rel="stylesheet">
<style>
  :root {
    --navy: #143f69;
    --navy-deep: #14204a;
    --sky: #d6e4f5;
    --ice: #dce8f7;
    --white: #ffffff;
    --ink: #333333;
    --accent-red: #c0282d;
  }
  * { margin: 0; padding: 0; box-sizing: border-box; }
  html, body { width: 1200px; height: 1200px; overflow: hidden; background: var(--white); }
  .canvas { position: relative; width: 1200px; height: 1200px; }
  .sticker-shape { position: absolute; inset: 0; }
  .headline, .cta-line { position: absolute; left: 0; width: 1200px; text-align: center; font-family: "Cinzel", serif; }
  .headline-small { top: 148px; font-size: 100px; color: var(--ice); letter-spacing: 2px; line-height: 1; }
  .headline-large { top: 258px; font-size: 128px; color: var(--ice); letter-spacing: 3px; line-height: 1; }
  .cta-phone { top: 418px; font-size: 64px; color: var(--navy); line-height: 1; }
  .cta-book { top: 524px; font-size: 58px; color: var(--ice); letter-spacing: 2px; line-height: 1; }
  .cta-free { top: 620px; font-size: 86px; color: var(--navy); letter-spacing: 6px; line-height: 1; font-weight: 500; }

  .book { position: absolute; left: 379px; top: 739px; width: 466px; height: 358px; border: 2px solid #111; background: var(--white); font-family: "Open Sans", sans-serif; overflow: hidden; }
  .book-back { position: absolute; left: 0; top: 0; width: 224px; height: 316px; padding: 14px 10px 0 20px; color: var(--ink); }
  .back-header { font-size: 5.5px; line-height: 7px; color: var(--accent-red); text-align: center; font-weight: 600; margin-bottom: 5px; }
  .back-copy { font-size: 5px; line-height: 6.5px; margin-bottom: 5px; text-align: justify; }
  .back-rule { height: 1px; background: var(--accent-red); margin: 8px 20px 12px; }
  .author-bio { display: flex; gap: 6px; margin-bottom: 6px; }
  .author-photo { width: 56px; height: 52px; flex: none; background: linear-gradient(160deg, #9fb3cc, #1f4aa0); }
  .author-bio .back-copy { margin: 0; }
  .back-firm { position: absolute; left: 20px; bottom: 24px; display: flex; align-items: center; gap: 5px; font-family: "Cinzel", serif; font-size: 11px; line-height: 12px; color: var(--navy-deep); }
  .firm-mark { width: 18px; height: 18px; background: var(--navy-deep); }
  .book-spine { position: absolute; left: 224px; top: 0; width: 12px; height: 316px; background: var(--navy-deep); }
  .spine-title { position: absolute; left: 236px; top: 110px; writing-mode: vertical-rl; font-size: 6px; color: var(--navy-deep); font-weight: 600; }
  .spine-author { position: absolute; left: 236px; top: 190px; writing-mode: vertical-rl; font-size: 5px; color: var(--navy-deep); }
  .book-front { position: absolute; left: 238px; top: 0; width: 226px; height: 316px; text-align: center; color: var(--navy-deep); }
  .front-author { font-size: 13px; margin-top: 12px; letter-spacing: -0.3px; }
  .front-title { font-size: 27px; font-weight: 800; line-height: 26px; margin-top: 4px; letter-spacing: -0.5px; }
  .front-photo { position: absolute; left: 2px; right: 2px; top: 92px; bottom: 0; background: linear-gradient(180deg, #e9eef2 0%, #9cc06a 45%, #6f9f3f 80%, #8fb85a 100%); }
  .book-bar { position: absolute; left: 0; right: 0; bottom: 0; height: 42px; background: var(--navy-deep); }
  .back-barcode-space { position: absolute; left: 139px; bottom: 0; width: 80px; height: 20px; background: var(--white); }
  .front-tagline { position: absolute; left: 238px; width: 226px; bottom: 6px; text-align: center; color: var(--white); font-size: 11px; line-height: 13px; }
</style>
</head>
<body>
<div class="canvas">
  <svg class="sticker-shape" width="1200" height="1200" viewBox="0 0 1200 1200" aria-hidden="true">
    <defs>
      <clipPath id="sticker-outline"><ellipse cx="600" cy="624" rx="600" ry="558"/></clipPath>
    </defs>
    <g clip-path="url(#sticker-outline)">
      <rect x="0" y="0" width="1200" height="1200" fill="var(--sky)"/>
      <rect x="0" y="0" width="1200" height="388" fill="var(--navy)"/>
      <rect x="0" y="508" width="1200" height="95" fill="var(--navy)"/>
    </g>
    <ellipse cx="600" cy="624" rx="599" ry="557" fill="none" stroke="var(--navy)" stroke-width="1.5"/>
  </svg>

  <div class="headline headline-small">Still have</div>
  <div class="headline headline-large">QUESTIONS?</div>
  <div class="cta-line cta-phone">CALL (907) 555-0148</div>
  <div class="cta-line cta-book">AND REQUEST OUR BOOK</div>
  <div class="cta-line cta-free">FOR FREE</div>

  <div class="book">
    <div class="book-bar"></div>
    <div class="back-barcode-space"></div>
    <div class="book-back">
      <p class="back-header">MOST DRIVERS WILL FACE A CRASH AT SOME POINT.</p>
      <p class="back-copy">Knowing your rights after a crash helps you act with confidence and avoid costly mistakes.</p>
      <p class="back-copy">This guide explains each step of an Alaska auto claim in plain language.</p>
      <div class="back-rule"></div>
      <div class="author-bio">
        <div class="author-photo" role="img" aria-label="Portrait photo of the author"></div>
        <p class="back-copy">Our founding attorney has spent two decades helping injured drivers recover fair compensation from insurers.</p>
      </div>
      <p class="back-copy">Since opening in Alaska, the firm has guided hundreds of local families through their claims.</p>
      <p class="back-copy">Most cases settle out of court, but careful preparation makes all the difference.</p>
      <div class="back-firm"><span class="firm-mark"></span><span>HARTWELL<br>LAW GROUP</span></div>
    </div>
    <div class="book-spine"></div>
    <div class="spine-title">CLEAR LANES AHEAD</div>
    <div class="spine-author">DANIEL R. HARTWELL</div>
    <div class="book-front">
      <div class="front-photo" role="img" aria-label="Photo of a smiling family lying on grass in a park with a small red car"></div>
      <p class="front-author">DANIEL R. HARTWELL</p>
      <h2 class="front-title">CLEAR LANES<br>AHEAD</h2>
    </div>
    <p class="front-tagline">THE RIGHT WAY TO HANDLE<br>YOUR AUTO ACCIDENT CLAIM</p>
  </div>
</div>
</body>
</html>
```